Flyer-Design für Schwimmtraining für Triathleten
Zielgruppe
Angebot
Schwimmen: als Personal Training, in Kleingruppen oder im Kraulkurs
Schwimmen: Videoanalysen
Triathlon: Trainingspläne, Leistungsdiagnostik
Zielgruppe des Flyers:
Triathleten jeder Leistungsklasse
Flyer ist a) als Auslage in Sportgeschäften, b) als Beilage in Wettkampftüten von Triathlonwettkämpfen gedacht
Aufgabenstellung
Triathleten sind tendenziell technisch orientierte Menschen, vergleichsweise wohlhabend. Schwimmen ist häufig eher die verhasste aber notwendige Teil der drei Disziplinen.
Bitte kein Standardformat für den Flyer.
Die Herausforderung bei einem Flyer als Beigabe zum Wettkampfbeutel: Überlicherweise wird der ganze Packen Werbung achtlos weggeworfen. Design und Format sollen dazu beitragen, dass der Flyer heraussticht und möglichst beachtet wird.
Grundsätzliche Infos: www.kelbrun42.de

```html
<!DOCTYPE html>
<html lang="de">
<head>
<meta charset="utf-8">
<title>Schwimmtraining Flyer</title>
<link rel="stylesheet" href="https://fonts.googleapis.com/css2?family=Quicksand:wght@400;500;600&display=swap">
<style>
  :root{
    --stage:#b7d2cf;
    --ink-dark:#04141b;
    --box-dark:rgba(34,44,48,.88);
    --panel:#d5e9ee;
    --accent:#3db8ea;
    --white:#ffffff;
    --photo-a:#7fa9a4;
    --photo-b:#c9bf95;
    --photo-c:#3f6f74;
  }
  *{margin:0;padding:0;box-sizing:border-box}
  html,body{width:1200px;height:775px;overflow:hidden;background:var(--stage)}
  body{font-family:"Quicksand",sans-serif;position:relative}
  .flyer{position:absolute;left:322px;top:28px;width:556px;height:720px;background:var(--ink-dark);overflow:hidden}
  .flyer-shapes{position:absolute;left:0;top:0}
  .abs{position:absolute}
  .intro-title{left:49px;top:14px;font-size:21px;font-weight:500;color:var(--white);letter-spacing:.2px}
  .intro-text{left:52px;top:51px;font-size:8.6px;line-height:11.6px;color:var(--white);font-weight:500}
  .slogan{left:380px;top:176px;width:130px;text-align:center;font-size:19px;line-height:24px;font-weight:500;color:var(--ink-dark);transform:rotate(-5deg)}
  .stat{left:357px;width:175px;text-align:center;color:var(--ink-dark)}
  .stat-number{font-size:56px;line-height:56px;font-weight:500}
  .stat-label{font-size:11.5px;font-weight:600;margin-top:2px}
  .stat-years{top:294px}
  .stat-sites{top:394px}
  .sites{left:357px;top:507px;width:175px;text-align:center;font-size:11px;line-height:14.5px;font-weight:600;color:var(--ink-dark)}
  .offer{left:57px;color:var(--white)}
  .offer h2{font-size:20.5px;font-weight:500;color:var(--accent);line-height:22px}
  .offer p{font-size:8.8px;line-height:12.5px;font-weight:600}
  .offer-service{top:368px}
  .offer-program{top:440px}
  .offer-analysis{top:512px;left:55px}
  .url{left:58px;top:686px;font-size:10px;font-weight:600;color:var(--white)}
  .brand{left:445px;top:674px;width:86px;text-align:center;font-size:12px;font-weight:600;color:var(--white);letter-spacing:.5px}
</style>
</head>
<body>
  <main class="flyer">
    <svg class="flyer-shapes" width="556" height="720" viewBox="0 0 556 720">
      <defs>
        <linearGradient id="poolTones" x1="0" y1="0" x2="1" y2="1">
          <stop offset="0" stop-color="var(--photo-b)"/>
          <stop offset=".45" stop-color="var(--photo-a)"/>
          <stop offset="1" stop-color="var(--photo-c)"/>
        </linearGradient>
      </defs>
      <polygon points="0,0 556,0 556,262 0,322" fill="url(#poolTones)" role="img" aria-label="Foto: lächelnder Schwimmer mit Badekappe und Schwimmbrille im Becken"/>
      <line x1="0" y1="322" x2="556" y2="262" stroke="var(--accent)" stroke-width="3"/>
      <polygon points="36,4 211,4 211,129 36,145" fill="var(--box-dark)"/>
      <polygon points="357,164 532,145 532,596 357,596" fill="var(--panel)" fill-opacity=".9"/>
    </svg>

    <h1 class="abs intro-title">Personal Training</h1>
    <p class="abs intro-text">Steigern Sie Ihre Schwimmkünste<br>mit einem persönlichem Trainer!<br>Alleine oder in Kleingruppen.</p>

    <p class="abs slogan">Make Water<br>Your<br>Friend</p>

    <div class="abs stat stat-years"><div class="stat-number">40</div><div class="stat-label">Jahre Erfahrung</div></div>
    <div class="abs stat stat-sites"><div class="stat-number">3</div><div class="stat-label">Standorte</div></div>
    <p class="abs sites">München,<br>Mallorca,<br>Liechtenstein</p>

    <section class="abs offer offer-service">
      <h2>Leistungsangebot</h2>
      <p>Wir bieten dir Schwimmtechnik-Training,<br>Kraulkurse, Trainingspläne und Leistungsdiagnostik an.</p>
    </section>
    <section class="abs offer offer-program">
      <h2>Programm</h2>
      <p>Wir erstellen Tainingspläne ganz auf Ihrer<br>Bedürfnisse angepasst.</p>
    </section>
    <section class="abs offer offer-analysis">
      <h2>Analysen und mehr...</h2>
      <p>Durch Videoanalysen kontrollieren wir Ihren<br>Fortschritt und passen somit Ihren Traininsplan an.</p>
    </section>

    <p class="abs url">www.kelbrun42.de</p>
    <p class="abs brand">KELBRUN42</p>
  </main>
</body>
</html>
```